Marwick Law Letterhead

We need a new letterhead design for a Law Firm. The address for the law firm is 4175 Calloway Avenue, Suite 200, Houston, Texas 77046. Phone Number: 832-614-2093; Fax Number: 832-307-1546. The logo is uploaded to the project.

```html
<!DOCTYPE html>
<html lang="en">
<head>
<meta charset="utf-8">
<title>Marwick Law Letterhead</title>
<link rel="stylesheet" href="https://fonts.googleapis.com/css2?family=Noto+Serif:wght@400;700&family=Roboto:wght@400&display=swap">
<style>
  :root {
    --navy: #1b2b52;
    --red: #d0141e;
    --ink: #333333;
    --paper: #ffffff;
  }
  html, body {
    margin: 0;
    padding: 0;
    width: 966px;
    height: 1200px;
    overflow: hidden;
    background: var(--paper);
  }
  .letterhead {
    position: relative;
    width: 966px;
    height: 1200px;
    background: var(--paper);
    font-family: "Roboto", Arial, sans-serif;
    color: var(--ink);
  }
  .brand {
    position: absolute;
    left: 63px;
    top: 108px;
  }
  .brand-name {
    font-family: "Noto Serif", Georgia, serif;
    font-weight: 700;
    font-size: 34px;
    line-height: 1.2;
    color: var(--navy);
    letter-spacing: 0.5px;
    margin: 0;
  }
  .contact {
    position: absolute;
    right: 200px;
    top: 80px;
    width: 360px;
    height: 110px;
    font-size: 12.5px;
    font-style: normal;
    line-height: 1.3;
  }
  .contact-row {
    position: absolute;
    right: 0;
    display: flex;
    align-items: center;
    gap: 10px;
    text-align: right;
    white-space: nowrap;
  }
  .contact-row svg {
    width: 18px;
    height: 18px;
    fill: var(--ink);
    flex: none;
  }
  .row-phone { top: 2px; }
  .row-fax { top: 38px; }
  .row-address { top: 70px; }
  .brand-mark {
    position: absolute;
    left: 784px;
    top: 61px;
    width: 118px;
    height: 118px;
    background: var(--navy);
  }
  .rule {
    position: absolute;
    height: 3px;
    background: var(--navy);
  }
  .rule-header { left: 63px; width: 703px; top: 198px; }
  .rule-footer { left: 63px; width: 839px; top: 1140px; }
  .footer {
    position: absolute;
    left: 63px;
    right: 64px;
    top: 1161px;
    display: flex;
    justify-content: space-between;
    font-family: "Noto Serif", Georgia, serif;
    font-weight: 700;
    font-size: 12px;
    letter-spacing: 2px;
    color: var(--ink);
    white-space: nowrap;
  }
  .tagline { text-transform: uppercase; }
  .edge {
    position: absolute;
    left: 0;
    right: 0;
    bottom: 0;
    height: 2px;
    background: var(--red);
  }
</style>
</head>
<body>
<div class="letterhead">
  <header>
    <div class="brand">
      <h1 class="brand-name">Marwick Law</h1>
    </div>

    <address class="contact">
      <div class="contact-row row-phone">
        <span>832-614-2093</span>
        <svg viewBox="0 0 24 24" aria-hidden="true"><path d="M6.6 10.8a15.1 15.1 0 0 0 6.6 6.6l2.2-2.2a1 1 0 0 1 1-.25 11.4 11.4 0 0 0 3.6.57 1 1 0 0 1 1 1V20a1 1 0 0 1-1 1A17 17 0 0 1 3 4a1 1 0 0 1 1-1h3.5a1 1 0 0 1 1 1c0 1.25.2 2.45.57 3.57a1 1 0 0 1-.25 1z"/></svg>
      </div>
      <div class="contact-row row-fax">
        <span>832-307-1546</span>
        <svg viewBox="0 0 24 24" aria-hidden="true"><path d="M6 2h12v5H6zM3 8h18a1 1 0 0 1 1 1v8h-4v5H6v-5H2V9a1 1 0 0 1 1-1zm5 7v5h8v-5zm1 1h6v1H9zm0 2h6v1H9z"/></svg>
      </div>
      <div class="contact-row row-address">
        <span>4175 Calloway Avenue<br>Suite 200, Houston, Texas 77046</span>
        <svg viewBox="0 0 24 24" aria-hidden="true"><path d="M12 2a7 7 0 0 0-7 7c0 5 7 13 7 13s7-8 7-13a7 7 0 0 0-7-7zm0 9.5A2.5 2.5 0 1 1 12 6.5a2.5 2.5 0 0 1 0 5z"/></svg>
      </div>
    </address>

    <div class="brand-mark" aria-hidden="true"></div>
    <div class="rule rule-header"></div>
  </header>

  <footer>
    <div class="rule rule-footer"></div>
    <div class="footer">
      <span class="tagline">Your recovery is our daily commitment</span>
      <span class="website">marwickinjury.com</span>
    </div>
  </footer>
  <div class="edge"></div>
</div>
</body>
</html>
```